Hofschild Design für Bauernhof
Zielgruppe
Urlaub auf dem Bauernhof mit Kühe
Ferienwohnungen und Zimmer
Zielgruppe Familie mit Kinder, Einzelübernachtungen, Monteure
Aufgabenstellung
Das Plakat ist ein Hofschild mit den Maßen 63cm hoch und 104cm breit
Text sollte beinhalten
Lindenauer Hof
Urlaub auf dem Bauernhof
Das Schild sollte ansprechend sein, vielleicht mit Tieren (Kühe, Kälbchen,Pony, Esel)
Aber auch nicht zu überladen, beim vorbeifahren sollte noch zu erkennen sein, dass wir der Lindenauer Hof sind
Habe Fotos angehängt für eine Vorstellung des Betriebs

```html
<!DOCTYPE html>
<html lang="de">
<head>
<meta charset="utf-8">
<title>Lindenauer Hof – Hofschild</title>
<link rel="stylesheet" href="https://fonts.googleapis.com/css2?family=Almendra:ital,wght@1,700&display=swap">
<style>
  :root {
    --frame-green: #d4df9e;
    --sign-white: #ffffff;
    --ink: #000000;
    --star-light: #ffff00;
    --star-dark: #efcd0c;
    --horse-tan: #caa08b;
    --horse-shade: #bf8a75;
  }
  html, body {
    margin: 0;
    padding: 0;
    overflow: hidden;
    background: var(--sign-white);
  }
  .sign {
    position: relative;
    width: 1200px;
    height: 727px;
    box-sizing: border-box;
    background: var(--sign-white);
    border: 16px solid var(--frame-green);
    overflow: hidden;
    font-family: "Almendra", Georgia, serif;
    font-style: italic;
    font-weight: 700;
    color: var(--ink);
  }
  .sign__title {
    position: absolute;
    left: 8px;
    top: 36px;
    margin: 0;
    font-size: 150px;
    line-height: 1;
    letter-spacing: 1px;
    white-space: nowrap;
    font-weight: 700;
  }
  .sign__offers {
    position: absolute;
    left: 11px;
    top: 256px;
    margin: 0;
    padding: 0;
    list-style: none;
    font-size: 59px;
    line-height: 97px;
    white-space: nowrap;
    z-index: 1;
  }
  .sign__stars {
    position: absolute;
    left: 10px;
    top: 543px;
    width: 620px;
    height: 144px;
  }
  .sign__animal {
    position: absolute;
    left: 700px;
    top: 300px;
    width: 468px;
    height: 395px;
    background: radial-gradient(ellipse at 55% 55%, var(--horse-tan) 0%, var(--horse-tan) 55%, var(--horse-shade) 100%);
    border-radius: 40px 40px 0 0;
  }
</style>
</head>
<body>
  <main class="sign">
    <h1 class="sign__title">Lindenauer Hof</h1>
    <ul class="sign__offers">
      <li>Urlaub auf dem Bauernhof</li>
      <li>Ferienwohnungen</li>
      <li>und Zimmer</li>
    </ul>
    <svg class="sign__stars" viewBox="0 0 620 144" aria-label="Vier Sterne">
      <defs>
        <symbol id="star" viewBox="-80 -80 160 146">
          <polygon fill="var(--star-dark)" points="0,-78 17.6,-24.3 74.2,-24.1 28.5,9.3 45.8,63.1 0,30 -45.8,63.1 -28.5,9.3 -74.2,-24.1 -17.6,-24.3"/>
          <polygon fill="var(--star-light)" points="0,0 0,-78 17.6,-24.3"/>
          <polygon fill="var(--star-light)" points="0,0 74.2,-24.1 28.5,9.3"/>
          <polygon fill="var(--star-light)" points="0,0 45.8,63.1 0,30"/>
          <polygon fill="var(--star-light)" points="0,0 -45.8,63.1 -28.5,9.3"/>
          <polygon fill="var(--star-light)" points="0,0 -74.2,-24.1 -17.6,-24.3"/>
        </symbol>
      </defs>
      <use href="#star" x="0" y="0" width="160" height="146"/>
      <use href="#star" x="151" y="0" width="160" height="146"/>
      <use href="#star" x="311" y="0" width="160" height="146"/>
      <use href="#star" x="469" y="0" width="160" height="146"/>
    </svg>
    <div class="sign__animal" role="img" aria-label="Illustration: freundliches braunes Pony mit orangem Halfter und Sattel"></div>
  </main>
</body>
</html>
```